Tech business card design

We need an amazing business card design for our new business 'Brakka' a marketing tech startup based in Sydney, Australia. We provide an online marketplace for businesses to search and buy advertising media, connect with service providers and learn more about marketing. We wish to communicate 'cool tech', reliability and professionalism and design based around our logo.

Target Market(s)

Business Owners

Contact Information for Business Card

Name
Position
Email Address
Website
Phone Number

Font styles to use
Other font styles liked:
• Avenir & Avenir Next

Colors

Designer to choose colors to be used in the design.

```html
<!DOCTYPE html>
<html lang="en">
<head>
<meta charset="utf-8">
<title>Brakka business card</title>
<link rel="stylesheet" href="https://fonts.googleapis.com/css2?family=Nunito+Sans:wght@400;600;700;800;900&display=swap">
<style>
  :root {
    --navy: #12133a;
    --teal: #62aebd;
    --teal-light: #8ccbd6;
    --white: #ffffff;
    --ink: #3f4048;
    --backdrop: #efefef;
  }
  * { margin: 0; padding: 0; box-sizing: border-box; }
  html, body {
    width: 1200px; height: 900px; overflow: hidden;
    background: var(--backdrop);
    font-family: "Nunito Sans", "Avenir Next", Avenir, sans-serif;
  }
  .card { position: absolute; width: 597px; height: 340px; overflow: hidden; }

  /* Front */
  .card-front { left: 302px; top: 85px; background: var(--navy); }
  .card-front .feature { position: absolute; left: 0; top: 0; width: 597px; height: 340px; }
  .card-front .brand {
    position: absolute; left: 358px; top: 139px;
    font-size: 62px; font-weight: 900; line-height: 1; letter-spacing: -0.5px;
    color: var(--white); white-space: nowrap;
  }
  .card-front .site {
    position: absolute; left: 359px; top: 194px;
    font-size: 16px; color: var(--teal); letter-spacing: 0.2px; white-space: nowrap;
  }

  /* Back */
  .card-back { left: 300px; top: 475px; background: var(--white); }
  .card-back .brand {
    position: absolute; left: 38px; top: 47px;
    font-size: 64px; font-weight: 900; line-height: 1; letter-spacing: -0.5px;
    color: var(--navy); white-space: nowrap;
  }
  .person { position: absolute; left: 392px; top: 140px; width: 164px; }
  .person-name {
    font-size: 20px; font-weight: 700; color: var(--navy); letter-spacing: 0.3px; line-height: 1;
    white-space: nowrap;
  }
  .person-name .surname { color: var(--teal); }
  .person-role {
    margin-top: 8px; height: 26px; padding-left: 5px;
    background: linear-gradient(90deg, var(--navy) 0%, var(--navy) 35%, var(--teal) 100%);
    color: var(--white); font-size: 15px; line-height: 26px; white-space: nowrap;
  }
  .divider {
    position: absolute; left: 40px; top: 207px; width: 515px; height: 1px; background: var(--navy);
  }
  .contacts { position: absolute; left: 40px; top: 220px; list-style: none; }
  .contacts li {
    display: flex; align-items: center; height: 25.5px;
    font-size: 16px; color: var(--ink); white-space: nowrap;
  }
  .contacts svg { width: 16px; height: 16px; margin-right: 9px; fill: var(--navy); }
  .base-band {
    position: absolute; left: 0; bottom: 0; width: 100%; height: 11px;
    background: linear-gradient(90deg, var(--navy) 0%, var(--navy) 40%, var(--teal) 65%, var(--teal-light) 100%);
  }
</style>
</head>
<body>

<section class="card card-front">
  <svg class="feature" viewBox="0 0 597 340">
    <defs>
      <linearGradient id="feature-tone" x1="0" y1="0" x2="1" y2="1">
        <stop offset="0" stop-color="#7cc1cf"/>
        <stop offset="0.55" stop-color="#5aa3b4"/>
        <stop offset="1" stop-color="#8fc9d4"/>
      </linearGradient>
    </defs>
    <path d="M0,0 L75,0 L318,147 Q338,165 318,183 L78,340 L0,340 Z" fill="#ffffff"/>
    <path role="img" aria-label="Photo of hands reviewing bar charts on a tablet beside a laptop and phone, in teal duotone"
          d="M0,0 L58,0 L300,147 Q318,165 300,183 L62,340 L0,340 Z" fill="url(#feature-tone)"/>
  </svg>
  <div class="brand">Brakka</div>
  <div class="site">www.brakkamedia.com.au</div>
</section>

<section class="card card-back">
  <div class="brand">Brakka</div>
  <div class="person">
    <div class="person-name">DANIEL <span class="surname">REEVE</span></div>
    <div class="person-role">Founder | Director</div>
  </div>
  <div class="divider"></div>
  <ul class="contacts">
    <li>
      <svg viewBox="0 0 16 16"><path d="M4 0h8a1.5 1.5 0 0 1 1.5 1.5v13A1.5 1.5 0 0 1 12 16H4a1.5 1.5 0 0 1-1.5-1.5v-13A1.5 1.5 0 0 1 4 0zm0.5 2v10.5h7V2zm3.5 11.3a0.9 0.9 0 1 0 0 1.8a0.9 0.9 0 0 0 0-1.8z"/></svg>
      +61 (0)400 555 201
    </li>
    <li>
      <svg viewBox="0 0 16 16"><path d="M1 3h14v1.2L8 9 1 4.2z"/><path d="M1 5.8l7 4.8 7-4.8V13H1z"/></svg>
      daniel@brakkamedia.com.au
    </li>
    <li>
      <svg viewBox="0 0 16 16"><circle cx="8" cy="8" r="7.5"/><path d="M4 5c1.5-1 3-0.5 3.5 0.5S6 8 5 9s-0.5 2.5-1.5 2C2.5 10 2.5 6 4 5zm5.5 4.5c1-0.5 3 0 3 1s-1.5 2.5-2.5 2.5-1.5-3-0.5-3.5z" fill="#ffffff"/></svg>
      www.brakkamedia.com.au
    </li>
  </ul>
  <div class="base-band"></div>
</section>

</body>
</html>
```